Coffee roasting needs homepage with web shop

small roasting (no cafe!) needs a simple website with a web shop. We sell coffee to dealers and end customers. The shop should be for end consumers as well as for B2B customers. A login should be available. The design should be modern and at the same time classic with subtle (dark) colors. We need the tabs "Coffee, Shop, Contact, Coffee, Coffee, Login, About Us, Imprint, Privacy" Logo nr 1 should be used from attached file

Target Market(s)

B2B

Number of Pages Required

5+ page

Font styles to use
Sans Serif

Colors

Designer to choose only greyscale colors for use in the design.

Requirements
Must have
• Webshop

```html
<!DOCTYPE html>
<html lang="en">
<head>
<meta charset="utf-8">
<title>Kornhaus Coffee Roasters</title>
<link rel="stylesheet" href="https://fonts.googleapis.com/css2?family=Playfair+Display:ital,wght@0,400;0,700;1,400;1,700&family=Roboto:wght@400;500&display=swap">
<style>
:root{
  --ink:#111111;
  --charcoal:#4a4b4b;
  --mist:#e2e3e7;
  --stone:#d6d6d6;
  --paper:#f4f4f4;
  --white:#ffffff;
  --muted:#555555;
  --body:#3a3a3a;
  --rule:rgba(255,255,255,.35);
}
*{box-sizing:border-box;margin:0;padding:0}
html,body{width:1200px;height:3083px;overflow:hidden}
body{position:relative;font-family:"Roboto",Arial,sans-serif;color:var(--body);background:var(--white)}
.abs{position:absolute}
.serif{font-family:"Playfair Display",Georgia,serif}
.btn{position:absolute;display:flex;align-items:center;justify-content:center;background:var(--ink);color:var(--white);font-size:13px;font-weight:500;letter-spacing:.3px;border-radius:25px;width:150px;height:49px}
.btn-small{position:absolute;display:flex;align-items:center;justify-content:center;background:var(--white);color:var(--ink);font-size:12px;border-radius:16px;width:84px;height:31px}
.photo{position:absolute;border-radius:50%;border:8px solid var(--white);box-shadow:14px 18px 22px rgba(0,0,0,.3)}
.social{position:absolute;width:21px;height:21px;border-radius:50%}

/* hero */
.hero{position:absolute;left:0;top:0;width:1200px;height:672px;background:var(--mist)}
.hero-panel{position:absolute;left:826px;top:0;width:374px;height:672px;background:var(--charcoal)}
.brand-mark{position:absolute;left:86px;top:25px;width:174px;height:174px;border-radius:50%;border:3px solid var(--ink);display:flex;align-items:center;justify-content:center;font-family:"Playfair Display",Georgia,serif;font-size:28px;color:var(--ink)}
.hero-title{left:86px;top:262px;font-size:53px;line-height:60px;font-style:italic;color:var(--ink)}
.hero-title b{font-weight:700}
.hero-text{left:86px;top:408px;width:360px;font-size:14px;line-height:21px}
.nav{top:26px;font-family:"Playfair Display",Georgia,serif;font-size:17px;color:var(--white)}
.hero-photo{left:579px;top:83px;width:492px;height:492px;background:radial-gradient(circle at 50% 50%,#7a4a2c 0%,#a8785a 35%,#f3efec 70%,#ffffff 100%)}
.slider-dot{left:1037px;top:628px;width:5px;height:5px;border-radius:50%;background:var(--white)}

/* products */
.products{position:absolute;left:0;top:672px;width:1200px;height:793px;background:var(--stone)}
.section-title{position:absolute;left:0;width:1200px;text-align:center;font-family:"Playfair Display",Georgia,serif;font-style:italic;font-weight:700;font-size:53px;color:var(--ink)}
.product{position:absolute;top:836px;width:330px;text-align:center}
.product-photo{position:relative;margin:0 auto;width:328px;height:328px;border-radius:50%;border:9px solid var(--white)}
.product-name{margin-top:24px;font-family:"Playfair Display",Georgia,serif;font-weight:700;font-size:29px;color:var(--muted)}
.product-text{margin-top:14px;font-size:14px;line-height:21px}

/* about */
.about{position:absolute;left:0;top:1465px;width:1200px;height:551px;background:var(--mist)}
.about-panel{position:absolute;left:0;top:1465px;width:371px;height:551px;background:var(--charcoal)}
.about-photo{left:177px;top:1545px;width:390px;height:390px;background:radial-gradient(circle at 40% 40%,#6b5a44 0%,#9a6c3e 40%,#b07a45 70%,#8a5a30 100%)}
.about-title{left:663px;top:1575px;font-family:"Playfair Display",Georgia,serif;font-style:italic;font-weight:700;font-size:53px;color:var(--ink)}
.about-text{left:663px;width:452px;font-size:14px;line-height:21px}

/* services */
.services{position:absolute;left:0;top:2016px;width:1200px;height:822px;background:radial-gradient(ellipse at 75% 30%,#6a6a6a 0%,#3a3a3a 40%,#1c1c1c 80%,#262626 100%)}
.services-title{top:2100px;color:var(--white)}
.services-intro{left:170px;top:2176px;width:860px;text-align:center;font-size:14px;line-height:22px;color:var(--white)}
.service{position:absolute;width:290px;text-align:center;color:var(--white)}
.service h3{font-family:"Playfair Display",Georgia,serif;font-weight:700;font-size:23px;line-height:30px}
.service p{font-size:14px;line-height:21px;margin-top:2px}
.service .btn-small{position:relative;margin:14px auto 0}
.rule-v{left:599px;top:2296px;width:1px;height:371px;background:var(--rule)}
.rule-h{left:212px;top:2483px;width:727px;height:1px;background:var(--rule)}
.contact-btn{left:477px;top:2727px;width:247px;height:48px;border-radius:25px;background:var(--white);color:var(--ink);font-size:14px;letter-spacing:.5px;display:flex;align-items:center;justify-content:center}

/* footer */
.footer{position:absolute;left:0;top:2838px;width:1200px;height:245px;background:var(--paper)}
.footer-heading{top:2889px;font-family:"Playfair Display",Georgia,serif;font-weight:700;font-size:18px;color:var(--body)}
.footer-link{font-size:14px;color:var(--body);letter-spacing:.3px}
.footer-mark{left:1002px;top:2891px;width:110px;height:110px;border-radius:50%;border:2px solid var(--ink);display:flex;align-items:center;justify-content:center;font-family:"Playfair Display",Georgia,serif;font-size:18px;color:var(--ink)}
.copyright{left:1002px;top:3015px;font-size:11px;letter-spacing:.6px}
</style>
</head>
<body>

<section class="hero">
  <div class="hero-panel"></div>
  <div class="brand-mark">Kornhaus</div>
  <h1 class="abs hero-title serif">Simple Roasted<br><b>Coffee Beans</b></h1>
  <p class="abs hero-text">Lorem ipsum dolor sit amet, consectetur adipiscing elit, sed do eiusmod tempor incididunt ut labore et dolore magna aliqua. Ut enim ad minim veniam,</p>
  <a class="btn" style="left:85px;top:520px">READ MORE</a>
  <div class="abs nav" style="left:868px">Sign Up &nbsp;/&nbsp; Log in</div>
  <div class="abs nav" style="left:1040px">Menu</div>
  <svg class="abs" style="left:1095px;top:32px" width="18" height="14" viewBox="0 0 18 14"><path d="M0 1h18M0 7h18M0 13h18" stroke="#fff" stroke-width="1.6"/></svg>
  <div class="photo hero-photo" role="img" aria-label="Roasted coffee beans on a white plate"></div>
  <span class="social" style="left:1149px;top:230px;border:1.5px solid #fff"></span>
  <span class="social" style="left:1149px;top:265px;border:1.5px solid #fff"></span>
  <span class="social" style="left:1149px;top:300px;border:1.5px solid #fff"></span>
  <svg class="abs" style="left:975px;top:620px" width="40" height="20" viewBox="0 0 40 20"><path d="M39 10H2M10 2L2 10l8 8" fill="none" stroke="#fff" stroke-width="1.5"/></svg>
  <div class="abs slider-dot"></div>
  <svg class="abs" style="left:1072px;top:620px" width="40" height="20" viewBox="0 0 40 20"><path d="M1 10h37M30 2l8 8-8 8" fill="none" stroke="#fff" stroke-width="1.5"/></svg>
</section>

<section class="products">
</section>
<h2 class="section-title" style="top:728px">Our Products</h2>
<svg class="abs" style="left:20px;top:988px" width="40" height="20" viewBox="0 0 40 20"><path d="M39 10H2M10 2L2 10l8 8" fill="none" stroke="#222" stroke-width="1.5"/></svg>
<svg class="abs" style="left:1137px;top:988px" width="40" height="20" viewBox="0 0 40 20"><path d="M1 10h37M30 2l8 8-8 8" fill="none" stroke="#222" stroke-width="1.5"/></svg>

<article class="product" style="left:85px">
  <div class="product-photo" role="img" aria-label="Close-up of dark roasted coffee beans" style="background:radial-gradient(circle at 40% 35%,#7a4a30 0%,#3d2217 55%,#b9906c 100%)"></div>
  <h3 class="product-name">Product Name</h3>
  <p class="product-text">Lorem ipsum dolor sit amet, consectetur adipiscing elit, sed do eiusmod tempor incididunt ut labore et dolore magna aliqua.</p>
</article>
<article class="product" style="left:433px">
  <div class="product-photo" role="img" aria-label="Roasted coffee beans on white" style="background:radial-gradient(circle at 50% 50%,#6e4328 0%,#9a6c4e 45%,#ffffff 85%)"></div>
  <h3 class="product-name">Product Name</h3>
  <p class="product-text">Lorem ipsum dolor sit amet, consectetur adipiscing elit, sed do eiusmod tempor incididunt ut labore et dolore magna aliqua.</p>
</article>
<article class="product" style="left:782px">
  <div class="product-photo" role="img" aria-label="Coffee beans resting on burlap" style="background:radial-gradient(circle at 50% 60%,#3a2418 0%,#6e4a30 40%,#9a7048 80%)"></div>
  <h3 class="product-name">Product Name</h3>
  <p class="product-text">Lorem ipsum dolor sit amet, consectetur adipiscing elit, sed do eiusmod tempor incididunt ut labore et dolore magna aliqua.</p>
</article>
<a class="btn" style="left:175px;top:1324px">READ MORE</a>
<a class="btn" style="left:523px;top:1324px">READ MORE</a>
<a class="btn" style="left:872px;top:1324px">READ MORE</a>

<section class="about"></section>
<div class="about-panel"></div>
<div class="photo about-photo" role="img" aria-label="Coffee beans cooling in a roaster drum"></div>
<h2 class="abs about-title">About Us</h2>
<p class="abs about-text" style="top:1662px">Lorem ipsum dolor sit amet, consectetur adipiscing elit, sed do eiusmod tempor incididunt ut labore et dolore magna aliqua. Ut enim ad minim veniam, quis nostrud exercitation ullamco laboris nisi ut aliquip ex ea commodo consequat.</p>
<p class="abs about-text" style="top:1767px">Lorem ipsum dolor sit amet, consectetur adipiscing elit, sed do eiusmod tempor incididunt ut labore et dolore magna aliqua.</p>
<a class="btn" style="left:663px;top:1846px">READ MORE</a>

<section class="services" role="img" aria-label="Dark roasted coffee beans spilling from a scoop"></section>
<h2 class="section-title services-title">Our Services</h2>
<p class="abs services-intro">Lorem ipsum dolor sit amet, consectetur adipiscing elit, sed do eiusmod tempor incididunt ut labore et dolore magna aliqua. Ut enim ad minim veniam, quis nostrud exercitation ullamco laboris nisi ut aliquip ex ea commodo consequat.</p>
<div class="abs rule-v"></div>
<div class="abs rule-h"></div>
<div class="service" style="left:262px;top:2316px"><h3>Light Roasting</h3><p>Lorem ipsum dolor sit amet, consectetur adipiscing elit.</p><a class="btn-small">more</a></div>
<div class="service" style="left:648px;top:2316px"><h3>Dark Roasting</h3><p>Lorem ipsum dolor sit amet, consectetur adipiscing elit.</p><a class="btn-small">more</a></div>
<div class="service" style="left:262px;top:2520px"><h3>Medium Roasting</h3><p>Lorem ipsum dolor sit amet, consectetur adipiscing elit.</p><a class="btn-small">more</a></div>
<div class="service" style="left:648px;top:2520px"><h3>Extra Dark Roasting</h3><p>Lorem ipsum dolor sit amet, consectetur adipiscing elit.</p><a class="btn-small">more</a></div>
<a class="abs contact-btn">CONTACT US FOR BUSINESS</a>

<footer class="footer"></footer>
<h4 class="abs footer-heading" style="left:86px">Usefull Links</h4>
<h4 class="abs footer-heading" style="left:446px">Contact Us</h4>
<h4 class="abs footer-heading" style="left:745px">Find Us On</h4>
<a class="abs footer-link" style="left:86px;top:2930px">Coffee</a>
<a class="abs footer-link" style="left:86px;top:2958px">Shop</a>
<a class="abs footer-link" style="left:86px;top:2986px">Contact</a>
<a class="abs footer-link" style="left:86px;top:3014px">About</a>
<a class="abs footer-link" style="left:227px;top:2930px">Imprint</a>
<a class="abs footer-link" style="left:227px;top:2958px">Privacy</a>
<p class="abs footer-link" style="left:446px;top:2930px;line-height:21px">58 Millbrook Lane,<br>Hartwell</p>
<p class="abs footer-link" style="left:446px;top:2994px;line-height:21px">hello@kornhaus-roasters.com<br>1-555-010-2287</p>
<span class="social" style="left:746px;top:2965px;border:1.5px solid #333"></span>
<span class="social" style="left:781px;top:2965px;border:1.5px solid #333"></span>
<span class="social" style="left:816px;top:2965px;border:1.5px solid #333"></span>
<div class="abs footer-mark">Kornhaus</div>
<p class="abs copyright">© COPYRIGHT 2019</p>

</body>
</html>
```